Business card for massage therapy company called Brook Fern Wellness

Need business card for massage therapy company called Brook Fern Wellness. Would like my logo on the front and the back of the card I have 3 options of logos and you can play with what looks better.

Would like this information displayed on the back of the card:

Marcus Ellery
Licensed Massage Therapist
321-555-0147
brookfern-example.com
brookfern_rest_

```html
<!DOCTYPE html>
<html lang="en">
<head>
<meta charset="utf-8">
<title>Brook Fern Wellness – Business Card</title>
<link rel="stylesheet" href="https://fonts.googleapis.com/css2?family=Montserrat:wght@400;500;700&display=swap">
<style>
  :root {
    --sage: #737b63;
    --clay: #bd8a64;
    --ink: #222222;
    --paper: #ffffff;
    --backdrop: #ece8e2;
  }
  * { margin: 0; padding: 0; box-sizing: border-box; }
  html, body {
    width: 1200px;
    height: 1200px;
    overflow: hidden;
    background: var(--backdrop);
    font-family: "Montserrat", sans-serif;
  }
  .card {
    position: absolute;
    left: 252px;
    width: 697px;
    height: 396px;
    background: var(--paper);
    border-radius: 22px;
    overflow: hidden;
    box-shadow: 0 6px 16px rgba(0,0,0,0.12);
  }
  .card--front { top: 179px; }
  .card--back { top: 625px; }

  .brand-mark {
    position: absolute;
    border: 1.5px solid var(--sage);
    border-radius: 50%;
  }
  .brand-name {
    position: absolute;
    text-align: center;
    color: var(--sage);
    font-weight: 400;
    text-transform: uppercase;
    line-height: 1.15;
  }
  .card--front .brand-mark {
    left: 283px; top: 86px;
    width: 142px; height: 142px;
  }
  .card--front .brand-name {
    left: 0; width: 100%;
    top: 240px;
    font-size: 38px;
    letter-spacing: 3px;
  }
  .card--front .brand-name span {
    display: block;
    font-size: 24px;
    letter-spacing: 9px;
  }

  .card--back .brand-mark {
    left: 128px; top: 115px;
    width: 104px; height: 104px;
  }
  .card--back .brand-name {
    left: 40px; width: 240px;
    top: 228px;
    font-size: 27px;
    letter-spacing: 2px;
  }
  .card--back .brand-name span {
    display: block;
    font-size: 17px;
    letter-spacing: 7px;
  }

  .divider {
    position: absolute;
    left: 322px; top: 63px;
    width: 1.5px; height: 272px;
    background: var(--sage);
  }
  .contact {
    position: absolute;
    left: 355px; top: 106px;
  }
  .contact__name {
    color: var(--sage);
    font-weight: 700;
    font-size: 31px;
    letter-spacing: 0.5px;
    text-transform: uppercase;
    line-height: 1;
  }
  .contact__role {
    margin-top: 12px;
    color: var(--clay);
    font-weight: 500;
    font-size: 17px;
    letter-spacing: 0.6px;
  }
  .contact__details {
    list-style: none;
    margin-top: 34px;
    color: var(--ink);
    font-size: 17px;
    letter-spacing: 0.3px;
  }
  .contact__details li { line-height: 29px; }

  .band {
    position: absolute;
    bottom: 0;
    height: 24px;
  }
  .band--sage { left: 0; width: 345px; background: var(--sage); }
  .band--clay { left: 351px; right: 0; background: var(--clay); }
</style>
</head>
<body>
  <section class="card card--front">
    <div class="brand-mark"></div>
    <h1 class="brand-name">Brook Fern<span>Wellness</span></h1>
  </section>

  <section class="card card--back">
    <div class="brand-mark"></div>
    <p class="brand-name">Brook Fern<span>Wellness</span></p>
    <div class="divider"></div>
    <div class="contact">
      <h2 class="contact__name">Marcus Ellery</h2>
      <p class="contact__role">Licensed Massage Therapist</p>
      <ul class="contact__details">
        <li>321-555-0147</li>
        <li>brookfern-example.com</li>
        <li>brookfern_rest_</li>
      </ul>
    </div>
    <div class="band band--sage"></div>
    <div class="band band--clay"></div>
  </section>
</body>
</html>
```